Hearthstone Larder Packaging Design

We are a new meat stick and beef jerky company called Hearthstone Larder. We are envisioning a pioneer in a raccoon hat on a rock outcropping looking down over the shenandoah valley and the blue ridge mountains of Virginia. I have included a really rough sketch to show what we are thinking.

```html
<!DOCTYPE html>
<html lang="en">
<head>
<meta charset="utf-8">
<title>Hearthstone Larder – Jerky &amp; Meat Stick Packaging</title>
<link rel="stylesheet" href="https://fonts.googleapis.com/css2?family=Arimo:wght@400;700&family=Bungee&family=Fira+Sans+Condensed:wght@400;600&display=swap">
<style>
  :root {
    --board: #ffffff;
    --frame: #c9c9c9;
    --note: #29a9e0;
    --ribbon: #9b2d3e;
    --ribbon-edge: #111111;
    --gold: #f6cf3c;
    --white: #ffffff;
    --watermark: rgba(150, 140, 80, 0.55);
    --forest-top: #a9b7c4;
    --forest-mid: #8a5a2a;
    --forest-low: #5e4a22;
  }
  * { margin: 0; padding: 0; box-sizing: border-box; }
  html, body {
    width: 1200px; height: 675px; overflow: hidden; background: var(--board);
  }
  .board { position: relative; width: 1200px; height: 675px; }
  .design-note {
    position: absolute; left: 24px; top: 111px; width: 146px;
    font-family: "Arimo", Arial, sans-serif; font-size: 7.4px; line-height: 10.5px;
    color: var(--note);
  }
  .design-note p { margin-bottom: 10.5px; }
  .design-note ol { list-style: none; }
  .design-note .key { font-weight: 700; }
  .mockup-frame {
    position: absolute; top: 36px; width: 398px; height: 597px;
    border: 1px solid var(--frame); background: var(--board);
  }
  .mockup-frame--jerky { left: 244px; }
  .mockup-frame--stick { left: 691px; }
  .package { position: absolute; left: 19px; top: 21px; width: 360px; height: 557px; }
  .brand-name { font-family: "Fira Sans Condensed", sans-serif; font-weight: 600; fill: var(--gold); }
  .tagline { font-family: "Fira Sans Condensed", sans-serif; font-size: 10.5px; fill: var(--white); }
  .product-title {
    font-family: "Bungee", sans-serif; fill: var(--ribbon);
    stroke: var(--white); stroke-width: 2; paint-order: stroke;
  }
  .batch-code { font-family: "Fira Sans Condensed", sans-serif; font-size: 13px; fill: var(--white); }
  .watermark { font-family: "Fira Sans Condensed", sans-serif; font-weight: 600; fill: var(--watermark); }
</style>
</head>
<body>
<main class="board">
  <section class="design-note">
    <p>Brief note on packaging design for Hearthstone Larder's Beef Jerky and Meat Sticks</p>
    <p>Overall design approach is to follow the brief provided. Elements and colors are used to make the packaging look 'Meaty', attractive on the shelf with high recall value, and relatable to the product.</p>
    <ol>
      <li class="key">1. These options showing design adopted for beef jerky and meat stick. MInimal change is proposed to build a strong brand recall.</li>
      <li class="key">2. Brand name is repeated as a watermark near the pioneer mascot, to establish stronger brand recall.</li>
      <li>3. The image of the 'Pioneer' has a more surreal treatment, with a halo giving it a God-like feel. It can be used to build up a brand story... attempt was to give this character a different feel from how such mascots are usually portrayed.</li>
      <li>4. There was no specific branding/logo brief provided. Elements used in this design can be adopted to any specifc requirements.</li>
      <li>5. Placeholder text is added for product features, descriptions or details. Design can be adopted to fit in more text, if required.</li>
    </ol>
  </section>

  <!-- Beef jerky pack -->
  <div class="mockup-frame mockup-frame--jerky">
    <svg class="package" viewBox="0 0 360 557">
      <defs>
        <linearGradient id="valleyJerky" x1="0" y1="0" x2="0" y2="1">
          <stop offset="0" stop-color="var(--forest-top)"/>
          <stop offset="0.22" stop-color="var(--forest-mid)"/>
          <stop offset="1" stop-color="var(--forest-low)"/>
        </linearGradient>
        <radialGradient id="haloJerky">
          <stop offset="0" stop-color="#fffbe0"/>
          <stop offset="0.6" stop-color="#f3d460" stop-opacity="0.8"/>
          <stop offset="1" stop-color="#f3d460" stop-opacity="0"/>
        </radialGradient>
      </defs>
      <path role="img" aria-label="Photo: autumn forest on the Blue Ridge Mountains above the Shenandoah Valley" fill="url(#valleyJerky)"
        d="M56,0 H304 A56,56 0 0 0 360,56 V501 A56,56 0 0 0 304,557 H56 A56,56 0 0 0 0,501 V56 A56,56 0 0 0 56,0 Z"/>
      <path class="ribbon-edge" fill="var(--ribbon-edge)" d="M87,0 C104,60 119,110 115,163 C112,230 84,290 90,350 C94,400 99,429 134,429 C194,429 244,404 307,399 C274,350 254,300 259,256 C262,200 244,140 284,0 Z"/>
      <path class="ribbon" fill="var(--ribbon)" d="M83,0 C100,60 115,110 111,163 C108,230 80,290 86,350 C90,400 95,425 130,425 C190,425 240,400 300,397 C270,350 250,300 255,256 C258,200 240,140 280,0 Z"/>
      <text class="brand-name" x="177" y="60" font-size="19" text-anchor="middle">HEARTHSTONE</text>
      <text class="brand-name" x="177" y="84" font-size="19" text-anchor="middle">LARDER</text>
      <text class="tagline" x="177" y="142" text-anchor="middle">Lorem ipsum dolar sit</text>
      <text class="tagline" x="177" y="155" text-anchor="middle">amat. La gazilaw sit amat.</text>
      <text class="product-title" x="170" y="231" font-size="52" text-anchor="middle" textLength="186" lengthAdjust="spacingAndGlyphs">BEEF</text>
      <text class="product-title" x="173" y="289" font-size="52" text-anchor="middle" textLength="252" lengthAdjust="spacingAndGlyphs">JERKY</text>
      <ellipse role="img" aria-label="Photo: slices of beef jerky" cx="176" cy="344" rx="86" ry="46" fill="#c95a6e"/>
      <text class="batch-code" transform="translate(354,453) rotate(-90)">Izn 001 wy</text>
      <ellipse role="img" aria-label="Illustration: glowing pioneer mascot in a raccoon hat on a rock" cx="58" cy="478" rx="34" ry="62" fill="url(#haloJerky)"/>
      <text class="watermark" x="86" y="503" font-size="68" textLength="210" lengthAdjust="spacingAndGlyphs">HEARTHSTONE</text>
      <text class="watermark" x="86" y="553" font-size="50" textLength="210" lengthAdjust="spacingAndGlyphs">LARDER</text>
    </svg>
  </div>

  <!-- Meat stick pack -->
  <div class="mockup-frame mockup-frame--stick">
    <svg class="package" viewBox="0 0 360 557">
      <defs>
        <linearGradient id="valleyStick" x1="0" y1="0" x2="0" y2="1">
          <stop offset="0" stop-color="var(--forest-top)"/>
          <stop offset="0.22" stop-color="var(--forest-mid)"/>
          <stop offset="1" stop-color="var(--forest-low)"/>
        </linearGradient>
        <radialGradient id="haloStick">
          <stop offset="0" stop-color="#fffbe0"/>
          <stop offset="0.6" stop-color="#f3d460" stop-opacity="0.8"/>
          <stop offset="1" stop-color="#f3d460" stop-opacity="0"/>
        </radialGradient>
      </defs>
      <path role="img" aria-label="Photo: autumn forest on the Blue Ridge Mountains above the Shenandoah Valley" fill="url(#valleyStick)"
        d="M56,0 H304 A56,56 0 0 0 360,56 V501 A56,56 0 0 0 304,557 H56 A56,56 0 0 0 0,501 V56 A56,56 0 0 0 56,0 Z"/>
      <path class="ribbon-edge" fill="var(--ribbon-edge)" d="M87,0 C104,60 119,110 115,163 C112,230 84,290 90,350 C94,400 99,429 134,429 C194,429 244,404 307,399 C274,350 254,300 259,256 C262,200 244,140 284,0 Z"/>
      <path class="ribbon" fill="var(--ribbon)" d="M83,0 C100,60 115,110 111,163 C108,230 80,290 86,350 C90,400 95,425 130,425 C190,425 240,400 300,397 C270,350 250,300 255,256 C258,200 240,140 280,0 Z"/>
      <text class="brand-name" x="177" y="60" font-size="19" text-anchor="middle">HEARTHSTONE</text>
      <text class="brand-name" x="177" y="84" font-size="19" text-anchor="middle">LARDER</text>
      <text class="tagline" x="177" y="142" text-anchor="middle">Lorem ipsum dolar sit</text>
      <text class="tagline" x="177" y="155" text-anchor="middle">amat. La gazilaw sit amat.</text>
      <text class="product-title" x="180" y="244" font-size="52" text-anchor="middle" textLength="198" lengthAdjust="spacingAndGlyphs">MEAT</text>
      <text class="product-title" x="180" y="297" font-size="52" text-anchor="middle" textLength="218" lengthAdjust="spacingAndGlyphs">STICK</text>
      <ellipse role="img" aria-label="Photo: a bundle of meat sticks" cx="184" cy="352" rx="92" ry="36" fill="#a8583f"/>
      <text class="batch-code" transform="translate(354,453) rotate(-90)">Izn 001 wy</text>
      <ellipse role="img" aria-label="Illustration: glowing pioneer mascot in a raccoon hat on a rock" cx="58" cy="478" rx="34" ry="62" fill="url(#haloStick)"/>
      <text class="watermark" x="86" y="503" font-size="68" textLength="210" lengthAdjust="spacingAndGlyphs">HEARTHSTONE</text>
      <text class="watermark" x="86" y="553" font-size="50" textLength="210" lengthAdjust="spacingAndGlyphs">LARDER</text>
    </svg>
  </div>
</main>
</body>
</html>
```